Halvercott Orthodontics business card

Using our existing logo (created with ArtFolio), please create a tasteful, contemporary business card. We are father and daughter orthodontists specializing in braces, clarafit, etc to design healthy, beautiful smiles for children, adolescents, and adults. We would like the design to be family-friendly but not childish.
The final design should include all of the information without looking cluttered (I hope! If necessary to achieve an optimal design, please consider making the card double-sided)
Purple, black, silver on a white card
Please include the following information:
Halvercott Orthodontics (logo)
Marguerite L. Halvercott, DMD
Douglas R. Halvercott, DMD

312 Bramblewood Street
North Andover, MA 01899
978.555.0142

847C Quarry Hollow Street
Methuen, MA 01898
978.555.0187

email frontdesk@halvercottortho.example
website www.halvercottortho.example

```html
<!DOCTYPE html>
<html lang="en">
<head>
<meta charset="utf-8">
<title>Halvercott Orthodontics business card</title>
<link rel="stylesheet" href="https://fonts.googleapis.com/css2?family=Open+Sans:wght@400;600;700&display=swap">
<style>
  :root {
    --purple: #662d91;
    --purple-deep: #5a2683;
    --purple-soft: #7a3fb0;
    --white: #ffffff;
    --silver: #8c8c8c;
    --backdrop: #2b2b2b;
  }
  * { box-sizing: border-box; margin: 0; padding: 0; }
  html, body {
    width: 1200px; height: 1015px; overflow: hidden;
    background: var(--backdrop);
    font-family: "Open Sans", Arial, sans-serif;
  }
  .sheet {
    width: 1200px; height: 1015px;
    display: flex; flex-direction: column; align-items: center; justify-content: center;
    gap: 60px;
  }
  .card {
    position: relative; width: 700px; height: 400px; overflow: hidden;
    background: var(--purple);
    box-shadow: 0 10px 30px rgba(0,0,0,.5);
  }
  /* front */
  .card--front { display: flex; align-items: center; justify-content: center; }
  .wordmark--front {
    display: flex; align-items: center; gap: 18px;
    color: var(--purple-soft); font-weight: 600; font-size: 40px; letter-spacing: 1px;
  }
  .wordmark__dot { width: 40px; height: 40px; border-radius: 50%; background: var(--purple-soft); }
  /* back */
  .card__art { position: absolute; inset: 0; }
  .wordmark--back {
    position: absolute; left: 430px; top: 130px; width: 260px;
    display: flex; align-items: center; gap: 10px;
    color: var(--purple); font-weight: 600; font-size: 21px; line-height: 1.15;
  }
  .wordmark--back .wordmark__dot { width: 24px; height: 24px; background: var(--purple); flex: none; }
  .details {
    position: absolute; left: 40px; top: 58px; color: var(--white);
    font-size: 15px; line-height: 1.32;
  }
  .details__names { font-weight: 700; font-size: 18px; line-height: 1.3; }
  .details__rule { width: 34px; height: 2px; background: var(--white); margin: 16px 0 12px; }
  .details__office + .details__office { margin-top: 16px; }
  .details__line { display: flex; align-items: center; gap: 7px; }
  .icon { width: 13px; height: 13px; flex: none; }
</style>
</head>
<body>
<main class="sheet">
  <section class="card card--front" aria-label="Card front">
    <div class="wordmark wordmark--front"><span class="wordmark__dot"></span>Halvercott Orthodontics</div>
  </section>

  <section class="card card--back" aria-label="Card back">
    <svg class="card__art" width="700" height="400" viewBox="0 0 700 400" aria-hidden="true">
      <rect width="700" height="400" fill="var(--purple)"/>
      <path d="M395 0 H700 V250 C640 270 560 275 510 260 A210 210 0 0 1 395 0 Z" fill="var(--silver)"/>
      <path d="M405 0 H700 V245 C640 262 565 265 520 255 A200 200 0 0 1 405 0 Z" fill="var(--white)"/>
    </svg>
    <div class="wordmark wordmark--back"><span class="wordmark__dot"></span>Halvercott Orthodontics</div>
    <div class="details">
      <p class="details__names">Marguerite L. Halvercott, DMD<br>Douglas R. Halvercott, DMD</p>
      <div class="details__rule"></div>
      <div class="details__office">
        <p>312 Bramblewood Street</p>
        <p>North Andover, MA 01899</p>
        <p class="details__line"><svg class="icon" viewBox="0 0 16 16"><path fill="#fff" d="M3 1l3 3-2 2c1 2 3 4 5 5l2-2 3 3-2 3C6 14 2 10 1 3z"/></svg>978.555.0142</p>
      </div>
      <div class="details__office">
        <p>847C Quarry Hollow Street</p>
        <p>Methuen, MA 01898</p>
        <p class="details__line"><svg class="icon" viewBox="0 0 16 16"><path fill="#fff" d="M3 1l3 3-2 2c1 2 3 4 5 5l2-2 3 3-2 3C6 14 2 10 1 3z"/></svg>978.555.0187</p>
      </div>
      <div class="details__rule"></div>
      <p class="details__line"><svg class="icon" viewBox="0 0 16 16"><rect x="1" y="3" width="14" height="10" fill="none" stroke="#fff" stroke-width="1.5"/><path d="M1 3l7 6 7-6" fill="none" stroke="#fff" stroke-width="1.5"/></svg>frontdesk@halvercottortho.example</p>
      <p class="details__line"><svg class="icon" viewBox="0 0 16 16"><circle cx="8" cy="8" r="6.5" fill="none" stroke="#fff" stroke-width="1.4"/><path d="M1.5 8h13M8 1.5c-3 3.5-3 9.5 0 13M8 1.5c3 3.5 3 9.5 0 13" fill="none" stroke="#fff" stroke-width="1.2"/></svg>www.halvercottortho.example</p>
    </div>
  </section>
</main>
</body>
</html>
```